Flyer für eine 24/7 Sicherheitslösung
Vielen, herzlichen Dank! KoRu hat sich sehr schnell und großartig in die Aufgabe zur Gestaltung eines Flyers/Folders für das Empfehlungsmarketing hineingearbeitet. Aus der Anforderungsbeschreibung für einen Flyer mit Rückantwortkarte sowie weiteren Informationen aus dem Briefing wurden selbstständig alle zur Verfügung stehenden Informationskanäle genutzt und in einem tollen Design umgesetzt. Änderungswünsche sind umgehend bearbeitet und mit eigenen Ideen optimiert worden. Toll!!! Meine uneingeschränkte Empfehlung.
Zielgruppe
Ich bin Technischer Berater zu den Themen energienahe Dienstleistungen, Photovoltaik, Stromspeicher, Smart Home und Gefahrenmeldeanlagen für häusliche Gefahren und Einbruch.
Zielgruppe für dieses Projekt sind Eigenheimbesitzer (Haus oder Eigentumswohnung) und kleine Gewerbetreibende, die ein Sicherheitsbedürfnis verspüren, Angst haben und bestenfalls die Vorzüge eines Smart Homes bereits für sich erkannt haben.
Aufgabenstellung
Es soll für das Empfehlungsmarketing ein Flyer zum Thema 24/7 Sicherheitslösung im Smart Home entwickelt werden.
Neben entsprechenden Informationen soll eine postalisch konforme Rückantwort-Karte (Bitte freimachen - falls Marke zur Hand) auf einem vierseitigen Flyer mit Abrisskante für die Rückantwort-Karte entstehen.
Es muss also möglich sein, einmal die Daten des Werbenden und einmal die Daten des Geworbenen mit seiner Unterschrift auf der Karte zu notieren. Die Unterschrift ist aus Verbraucher-/Datenschutzgründen notwendig, damit diese Privatperson somit ihre Erlaubnis erteilt, dass sie von mir kontaktiert werden darf.
Und natürlich müssen sich auch meine Kontaktdaten auf dem Flyer wiederfinden - nur der Vollständigkeit halber. :-)
Ziel ist es einerseits, Verbrauchern den Flyer zur Weitergabe an Freunde, Nachbarn etc. und andererseits den Flyer an Gewerbetreibende zu reichen.
Freundschaftswerbung soll mit je 25 Euro für den Werber und den Geworbenen (Familienmitglieder im gleichen Haushalt ausgeschlossen) bei erfolgreicher Vermittlung, also Zustandekommen eines Auftrags, honoriert werden.
Bei Gewerbetreibende wird jede erfolgreiche Vermittlung, also mit Zustandekommen eines Auftrags, mit 50,00 Euro zzgl. MwSt. honoriert werden. Der Mindestauftragswert soll bei 950,00 Euro (brutto) liegen.
Zur groben Orientierung oder Anregung kann die Website https://schutzsysteme.brelvon.de eingesehen werden.
Die Begrifflichkeiten Sicherheit und Lösung sollen im Vordergrund kommuniziert werden. Die 24/7 Sicherheitslösung bezieht sich auf eine Gefahrenmeldeanlage, vorrangig zur Verhinderung von Schäden aus häuslichen Gefahren wie Rauch, Feuer, Wasser und Gas sowie Einbruch und Diebstahl mit Aufschaltung auf eine Notrufserviceleitstelle. Unter Umständen ist sogar eine staatliche Förderung gegeben.
Es kann auch auf Presse- und Bildmaterial des Herstellers FALKOR-Systemtechnik (http://kurzlnk.de/7QwrtZm) bzw. Pressebilder de Pol..

```html
<!DOCTYPE html>
<html lang="de">
<head>
<meta charset="utf-8">
<title>Flyer 24/7 Sicherheitslösungen</title>
<link href="https://fonts.googleapis.com/css2?family=Jost:wght@300;400;600;700;800&display=swap" rel="stylesheet">
<style>
:root{
  --navy:#053b91;
  --sky:#4d7dc7;
  --bar:#5a86cc;
  --orange:#f08a24;
  --white:#ffffff;
  --ink:#1d1d1b;
  --photo-a:#8f7a5e;
  --photo-b:#4a4034;
}
*{margin:0;padding:0;box-sizing:border-box}
html,body{width:1200px;height:595px;overflow:hidden;background:#d6d6d6}
body{font-family:'Jost',sans-serif;color:var(--white);position:relative}
.flyer{position:absolute;inset:0;overflow:hidden}
.panel{position:absolute;top:0;height:595px}
.panel-info{left:0;width:402px;background:var(--navy)}
.panel-photo{left:402px;width:402px;background:linear-gradient(160deg,#cfc9bd 0%,var(--photo-a) 40%,var(--photo-b) 100%)}
.panel-reply{left:804px;width:396px;background:var(--sky)}

.headline{position:absolute;left:0;top:17px;width:437px;height:66px;background:var(--orange);padding:8px 0 0 28px;font-size:21.5px;line-height:24px;font-weight:400;z-index:3}
.headline b{font-weight:700}

.intro{position:absolute;left:28px;top:113px;width:318px;font-size:11px;line-height:13px;font-weight:300}
.intro p{margin-bottom:14px}
.intro b{font-weight:600}
.intro i{font-weight:600;font-style:italic}

.section-bar{position:absolute;top:338px;height:26px;background:var(--bar);font-size:13.4px;font-weight:300;padding:4px 0 0 0;line-height:18px}
.section-bar b{font-weight:600}
.bar-left{left:0;width:193px;padding-left:28px}
.bar-right{left:216px;width:186px;padding-left:8px}

.column{position:absolute;top:382px;font-size:11px;line-height:13.2px;font-weight:300}
.column p{margin-bottom:19px}
.col-left{left:28px;width:156px}
.col-right{left:224px;width:146px}

.contact-box{position:absolute;left:17px;top:506px;width:178px;height:66px;background:var(--orange);padding:8px 0 0 11px;font-size:12px;line-height:16.4px;font-weight:400}
.contact-box b{font-weight:600}

.photo-area{position:absolute;inset:0}
.service{position:absolute;left:38px;width:152px;background:var(--navy);padding:9px 4px 0 22px;font-weight:300;font-size:9.8px;line-height:11.8px}
.service h3{font-size:13.6px;font-weight:600;line-height:16px;margin-bottom:4px}
.service-secure{top:80px;height:96px}
.service-home{top:203px;height:108px}
.service-care{top:338px;height:100px}
.service-video{top:459px;height:119px}
.service-icon{position:absolute;left:9px;width:46px;height:46px;border-radius:50%;background:var(--sky);display:flex;align-items:center;justify-content:center;z-index:2}

.reply-card{position:absolute;left:0;top:0;width:396px;height:298px;background:var(--white);color:var(--ink);border-left:1px dashed #9a9a9a;border-bottom:1px dashed #9a9a9a}
.form{position:absolute;left:11px;top:11px;width:197px}
.form-title{background:var(--navy);color:var(--white);font-size:7px;font-weight:600;height:12px;padding:1px 4px;letter-spacing:.2px}
.form-row{display:flex;border-bottom:0.8px solid #555;height:20px;font-size:5.4px;padding-top:4px}
.form-row span{width:88px;padding-left:3px}
.form-sign{height:34px;display:flex;align-items:flex-end;font-size:5.4px;padding:0 0 1px 3px;border-bottom:0.8px solid #555}
.form-gap{height:6px}
.consent{font-size:4.6px;color:var(--orange);text-align:right;line-height:6px;margin-top:-14px;padding-bottom:4px}
.form-second .form-sign{border-bottom:none;align-items:flex-start;padding-top:3px;height:24px}
.divider{position:absolute;left:242px;top:26px;width:2px;height:230px;background:var(--ink)}
.postmark{position:absolute;left:266px;top:29px;font-size:6px;line-height:8px}
.postmark b{font-weight:600;display:flex;align-items:center;gap:3px}
.postmark b::after{content:"";width:6px;height:6px;border-radius:50%;background:var(--ink)}
.postmark i{font-size:4.8px;letter-spacing:.4px;font-weight:600}
.stamp{position:absolute;left:325px;top:13px;width:54px;height:70px;border:1px dashed #333;font-size:8px;line-height:10px;text-align:center;padding-top:13px}
.address{position:absolute;left:263px;top:150px;font-size:12px;line-height:14px;font-weight:300}
.address p+p{margin-top:13px}

.reward-title{position:absolute;left:31px;top:328px;font-size:21px;font-weight:300}
.reward-title b{font-weight:600}
.reward{position:absolute;top:368px;width:152px;height:97px;background:var(--navy);border:2px solid var(--white);padding:2px 0 0 8px}
.reward .amount{font-size:45px;font-weight:800;line-height:48px;letter-spacing:-1px}
.reward .label{font-size:13px;font-weight:600;line-height:16px;text-align:center;padding-right:8px}
.reward-friends{left:31px}
.reward-business{left:199px}
.terms{position:absolute;left:31px;top:494px;width:345px;font-size:8px;line-height:11px;font-weight:300}
.terms small{font-size:5px}
.terms p+p{margin-top:10px}
</style>
</head>
<body>
<main class="flyer">

  <section class="panel panel-info">
    <h1 class="headline">24/7 <b>Sicherheitslösungen</b> gegen<br>häusliche <b>Gefahren und Einbruch</b></h1>

    <div class="intro">
      <p>Die neue Generation <i>Sicherheitstechnik</i> ist nicht nur eine professionelle <i>Alarmanlage</i>, die zuverlässig bei einem <b>Einbruch</b> oder <b>Überfall</b> und häuslichen <b>Gefahren</b>, wie <b>Rauch</b>, <b>Gas</b>, <b>Feuer</b> und <b>Wasseraustritt</b> informiert.</p>
      <p>Die im <b>Alarmsystem</b> integrierte <b>Videoüberwachung</b> sorgt dafür, dass Sie alles im <b>Blick</b> haben - auch von <b>unterwegs</b>.</p>
      <p>Als altersgerechtes <b>Assistenzsystem</b> unterstützt dieselbe <b>Sicherheitslösung</b> ebenso bei <b>medizinischen Notfällen</b> und sorgt in Ihrem <b>Smart Home</b> für <b>Komfort</b> und <b>Sicherheit</b>.</p>
      <p>Und sollte doch einmal etwas passieren, hilft die angeschlossene <b>Notrufservice-Leitstelle</b> sofort weiter, informiert Sie, Ihre Nachbarn oder <b>Polizei und Feuerwehr</b>.</p>
    </div>

    <h2 class="section-bar bar-left">Flexible <b>Leistungen</b></h2>
    <h2 class="section-bar bar-right">Praktische <b>Lösungen</b></h2>

    <div class="column col-left">
      <p>Wir verstehen Sicherheit als Dienstleistung. Sie bestimmen Ihre Lebensbereiche. Wir sorgen für die geeignete Ausstattung.</p>
      <p>Sie fühlen sich sicher und wählen zwischen Kauf oder bequemen Service-Abonnement!</p>
    </div>
    <div class="column col-right">
      <p>Einbruchschutz oder Gefahren-meldung? Sicherheitstechnik schützt vor Gefahren.</p>
      <p>Gefahrenmeldungen werden direkt und unmittelbar an eine 24/7 besetzte Notrufserivce-Leitstelle gesendet.</p>
      <p>Videoüberwachung ist sinnvoll für das "Gute Gefühl" und die Beweissicherung!</p>
    </div>

    <div class="contact-box">
      <b>Jetzt kostenfreie Beratung:</b><br>
      Telefon 04521 338 410<br>
      <b>oder unter</b> info@senvalo.de
    </div>
  </section>

  <section class="panel panel-photo">
    <div class="photo-area" role="img" aria-label="Foto eines durchwühlten Raums nach einem Einbruch: umgestürzter Blumentopf mit Erde auf der Fensterbank, offene Schublade mit Kleidung"></div>

    <div class="service-icon" style="top:57px">
      <svg width="22" height="22" viewBox="0 0 24 24" fill="none" stroke="#fff" stroke-width="1.3"><path d="M6 17V11a6 6 0 0 1 12 0v6l2 2H4z"/><path d="M10 21h4"/><path d="M12 3v2"/></svg>
    </div>
    <article class="service service-secure">
      <h3>Alarmschutz</h3>
      Einbruch-, Überfall- und Gefahrenmeldeanlagen Europanorm zertifiziert für Heim und Gewerbe
    </article>

    <div class="service-icon" style="top:183px">
      <svg width="22" height="22" viewBox="0 0 24 24" fill="none" stroke="#fff" stroke-width="1.3"><rect x="6" y="3" width="10" height="18" rx="2"/><path d="M13 11l4 2-2 5h-4z"/></svg>
    </div>
    <article class="service service-home">
      <h3>Wohnsteuerung</h3>
      Smart Home Anlagen sind Betriebssysteme fürs Zuhause Licht, Zutritt, Klima, Unterhaltung und immer auch Sicherheit
    </article>

    <div class="service-icon" style="top:323px">
      <svg width="22" height="22" viewBox="0 0 24 24" fill="none" stroke="#fff" stroke-width="1.3"><circle cx="12" cy="8" r="4"/><path d="M4 21c1-4 4-6 8-6s7 2 8 6"/><path d="M6 14h3"/></svg>
    </div>
    <article class="service service-care">
      <h3>Wohnassistenz</h3>
      Assistenzsysteme für altersgerechtes Wohnen Individuell gestaltbar mit Hausnotruffunktion
    </article>

    <div class="service-icon" style="top:448px">
      <svg width="22" height="22" viewBox="0 0 24 24" fill="none" stroke="#fff" stroke-width="1.3"><path d="M3 8h18v3a9 5 0 0 1-18 0z"/><circle cx="12" cy="12" r="3"/></svg>
    </div>
    <article class="service service-video">
      <h3>Videoblick</h3>
      Unterwegs Zuhause sein Videotechnik schafft Sicherheit, Gewissheit und auch Beweise<br>Schön, wenn alles in Ordnung ist
    </article>
  </section>

  <section class="panel panel-reply">
    <div class="reply-card">
      <div class="form">
        <div class="form-title">Werbende/r</div>
        <div class="form-row"><span>Name</span><span>Vorname</span></div>
        <div class="form-row"><span>Strasse, Nr.</span><span>PLZ, Ort</span></div>
        <div class="form-row" style="height:28px"><span>Telefon</span><span>E-Mail</span></div>
        <div class="form-sign" style="height:10px;border-bottom:none">Unterschrift</div>
        <div class="form-title">Geworbene/r</div>
        <div class="form-gap"></div>
        <div class="form-row"><span>Name</span><span>Vorname</span></div>
        <div class="form-row"><span>Strasse, Nr.</span><span>PLZ, Ort</span></div>
        <div class="form-row" style="height:28px"><span>Telefon</span><span>E-Mail</span></div>
        <div class="form-second"><div class="form-sign">Unterschrift</div></div>
        <p class="consent">Mit Ihrer Unterschrift erklären Sie sich einverstanden,<br>zu Beratungs- und Werbezwecken kontaktiert zu werden.</p>
      </div>
      <div class="divider"></div>
      <div class="postmark"><b>Postdienst</b><i>WERBEANTWORT</i></div>
      <div class="stamp">Bitte frei<br>machen<br>falls Marke<br>zur Hand</div>
      <div class="address">
        <p>senvalo<br>security solutions<br>management</p>
        <p>Lindenweg 8<br>D-24107 Feldhusen</p>
      </div>
    </div>

    <h2 class="reward-title">Ihre <b>Empfehlung</b> ist uns was <b>Wert!</b></h2>
    <div class="reward reward-friends">
      <div class="amount">25€</div>
      <div class="label">Für Sie und Ihre<br>Bekannten!</div>
    </div>
    <div class="reward reward-business">
      <div class="amount">50€</div>
      <div class="label">Zusatzverdienst<br>für Ihre Firma!</div>
    </div>
    <div class="terms">
      <p>Eine Freundschaftswerbung wird mit je 25 Euro für den Werber und den Geworbenen <small>(Familienmitglieder im gleichen Haushalt ausgeschlossen)</small> bei erfolgreicher Vermittlung, also Zustandekommen eines Auftrags, honoriert.</p>
      <p>Bei Gewerbetreibenden wird jede erfolgreiche Vermittlung, also mit Zustandekommen eines Auftrags mit einem Mindestauftragswert von 950,00 Euro (brutto), mit 50,00 Euro zzgl. MwSt. honoriert.</p>
    </div>
  </section>

</main>
</body>
</html>
```